VELMOR MOBILE APP RE-DESIGN - MINIMALISTIC AND CLEAN DESIGN

We are looking for a design that is minimalistic, clean, modern and appealing to millennials...
IMPORTANT: This is NOT a logo design nor a website design... This is for a mobile App Design. You can download our app on iOS or Android: "VELMOR iLINKUP"

We are attaching our new logo and some apps that we like the design, colors, shadows, 3d effects, style, etc...

For content, you can check our website: www.velmor.example

Please feel free to ask questions, it's very important that you understand the project. Thank you

Also, check out this website...we do like the design and colors: https://brindlo.example/
Updates

This is not for a logo design... this is for a mobile app design.... please download our app on iOS: VELMOR iLINKUP... THANK YOU

Target Market(s)

20 - 35
60% Male 40 Female

Requirements
Must have
• great graphics, color shadows for 3d effects, great colors with transparency, IMPORTANT: CLEAN DESIGN, Minimalistic.

```html
<!DOCTYPE html>
<html lang="en">
<head>
<meta charset="utf-8">
<title>Velmor Redesign Concept</title>
<link href="https://fonts.googleapis.com/css2?family=Noto+Sans:wght@400;500;600;700&display=swap" rel="stylesheet">
<style>
:root{
  --blue:#1f4fe0;
  --blue-deep:#0b2fc4;
  --blue-soft:#e8eeff;
  --ink:#1b1d2a;
  --muted:#8a8fa3;
  --line:#e6e8f0;
  --bg:#ffffff;
  --screen:#ffffff;
  --shadow:0 10px 30px rgba(31,79,224,.12);
  --card-shadow:0 4px 14px rgba(20,30,70,.09);
  --pink:#ff3d8b;
  --green:#3fd97f;
  --orange:#f28b1e;
  --brand-green:#1e6b47;
  --brand-gold:#f2b705;
  --photo:#b9c0cc;
}
*{box-sizing:border-box;margin:0;padding:0}
html,body{width:1200px;height:2346px;overflow:hidden;background:var(--bg)}
body{position:relative;font-family:"Noto Sans",sans-serif;color:var(--ink)}
.page-title{position:absolute;top:30px;left:0;width:1200px;text-align:center;color:var(--blue);font-size:15px;font-weight:600}
.screen{position:absolute;width:270px;height:560px;background:var(--screen);border-radius:34px;box-shadow:0 0 0 1px var(--line),var(--shadow);overflow:hidden}
.caption{position:absolute;width:270px;text-align:center;font-size:13px;color:var(--ink)}
.col1{left:73px}.col2{left:465px}.col3{left:857px}
.row1{top:95px}.row2{top:820px}.row3{top:1535px}
.cap1{top:682px}.cap2{top:1407px}.cap3{top:2122px}

.brand{display:flex;flex-direction:column;align-items:center;gap:6px}
.brand-dot{width:22px;height:22px;border-radius:50%;background:var(--blue)}
.brand-sm{position:absolute;top:26px;left:20px;display:flex;align-items:center;gap:5px;font-size:10px;font-weight:700;color:var(--blue)}
.brand-sm .brand-dot{width:16px;height:16px}
.search{position:absolute;top:26px;right:20px;width:16px;height:16px}
.topbar{position:absolute;top:24px;left:0;width:100%;text-align:center;font-size:10px;color:var(--ink)}
.back{position:absolute;top:24px;left:18px;width:14px;height:14px}
.center-text{text-align:center;font-size:12px;line-height:1.4}
.center-text b{display:block;font-size:15px}

.btn{display:inline-block;background:var(--blue);color:#fff;font-size:11px;font-weight:600;padding:8px 0;width:100px;text-align:center;border-radius:16px;box-shadow:0 6px 14px rgba(31,79,224,.35)}
.btn.white{background:#fff;color:var(--blue);box-shadow:none}

/* walkthrough */
.walk .brand{position:absolute;top:70px;left:0;width:100%}
.walk .band{position:absolute;left:20px;right:20px;top:300px;height:230px;border-radius:10px;background:linear-gradient(160deg,var(--blue),var(--blue-deep))}
.walk .intro{position:absolute;left:38px;right:38px;top:190px;height:250px;background:#fff;border-radius:6px;box-shadow:var(--card-shadow);padding:22px 16px;text-align:center}
.walk .intro h3{font-size:13px;margin-bottom:10px}
.walk .intro p{font-size:9.5px;line-height:1.5;color:#45495a}
.walk .cta{position:absolute;top:462px;left:0;width:100%;text-align:center}

/* forms */
.form-brand{position:absolute;top:62px;left:0;width:100%}
.form-card{position:absolute;left:40px;right:0;background:#fff;box-shadow:var(--card-shadow);border-radius:6px 0 0 6px}
.form-accent{position:absolute;left:0;width:40px;background:var(--blue)}
.field{height:34px;border-bottom:1px solid var(--line);font-size:9.5px;color:var(--ink);padding:12px 14px;position:relative}
.field:last-child{border-bottom:none}
.field svg{position:absolute;right:14px;top:12px}
.forgot{position:absolute;right:16px;font-size:9.5px;color:var(--blue);font-weight:600}
.form-cta{position:absolute;left:0;width:100%;text-align:center}
.switch-link{position:absolute;left:0;width:100%;text-align:center;font-size:9.5px;color:var(--muted)}
.switch-link b{color:var(--blue)}

/* home */
.banner{position:absolute;top:78px;left:26px;right:26px;height:96px;border-radius:8px;background:linear-gradient(135deg,var(--blue),#3c6bff);box-shadow:0 8px 18px rgba(31,79,224,.35);padding:20px 12px;color:#fff;font-size:12px;font-weight:700;line-height:1.35}
.banner .stripe{position:absolute;right:22px;top:22px;width:12px;height:48px;background:var(--pink);border-radius:3px;transform:rotate(18deg)}
.peek-l{position:absolute;left:8px;top:88px;width:10px;height:76px;background:var(--pink);border-radius:4px}
.peek-r{position:absolute;right:8px;top:88px;width:10px;height:76px;background:var(--green);border-radius:4px}
.dots{position:absolute;top:186px;left:0;width:100%;display:flex;justify-content:center;gap:3px}
.dots i{width:4px;height:4px;border-radius:50%;background:var(--line)}
.dots i.on{background:var(--blue);width:10px;border-radius:2px}
.section-head{display:flex;justify-content:space-between;font-size:10px;font-weight:700}
.section-head span{color:var(--blue);font-size:8.5px;font-weight:600}
.list{position:absolute;left:20px;right:20px}
.item{height:58px;background:#fff;border-radius:6px;box-shadow:var(--card-shadow);margin-top:10px;padding:9px 10px;position:relative}
.item-name{font-size:11px;font-weight:700}
.item-name em{font-style:normal;color:var(--blue);font-size:8.5px;font-weight:600;margin-left:4px}
.item-meta{font-size:8px;color:var(--muted);margin-top:2px;display:flex;align-items:center;gap:3px}
.mini-avatar{width:9px;height:9px;border-radius:50%;background:var(--photo)}
.badge{position:absolute;right:12px;top:13px;width:32px;height:32px}
.badge.round{border-radius:50%;background:var(--brand-green)}
.badge.square{border-radius:3px;background:var(--orange)}
.badge.gold{border-radius:3px;background:var(--brand-gold)}

.nav{position:absolute;bottom:0;left:0;width:100%;height:52px;background:#fff;box-shadow:0 -4px 14px rgba(20,30,70,.06);display:flex;justify-content:space-around;align-items:center;padding:0 10px}
.nav-item{display:flex;flex-direction:column;align-items:center;gap:2px;font-size:6.5px;font-weight:700;color:var(--blue);width:36px}
.nav-plus{width:28px;height:28px;border-radius:50%;background:var(--blue);margin-top:-22px;box-shadow:0 6px 12px rgba(31,79,224,.4);display:flex;align-items:center;justify-content:center}

/* details */
.detail-body{position:absolute;top:56px;left:18px;right:18px}
.detail-title{font-size:13px;font-weight:700}
.detail-sub{font-size:9px;color:#45495a;margin-top:4px;width:150px;line-height:1.4}
.detail-img{position:absolute;right:0;top:2px;width:44px;height:44px;border-radius:3px;background:var(--orange)}
.label{font-size:10px;font-weight:700;margin-top:14px}
.added{margin-top:6px;height:32px;border-radius:6px;box-shadow:var(--card-shadow);display:flex;align-items:center;gap:8px;padding:0 10px;font-size:9px;position:relative}
.added .ring{position:absolute;right:10px;width:9px;height:9px;border-radius:50%;border:1px solid var(--muted)}
.avatar{width:18px;height:18px;border-radius:50%;background:var(--photo)}
.tags{display:flex;flex-wrap:wrap;gap:6px;margin-top:8px}
.tag{background:var(--blue);color:#fff;font-size:8px;border-radius:10px;padding:4px 0;width:60px;text-align:center}
.para{font-size:8.5px;line-height:1.5;color:#45495a;margin-top:4px}
.link{font-size:8.5px;color:var(--blue);text-decoration:underline;margin-top:8px;display:block}

/* add new */
.add-card{position:absolute;left:40px;right:0;top:74px;background:#fff;box-shadow:var(--card-shadow);border-radius:6px 0 0 6px}
.add-card .field{height:40px}
.add-card .field.tall{height:62px}
.add-card .field.img{display:flex;align-items:center;gap:6px;padding:0 14px}
.img-icon{width:16px;height:16px;border-radius:3px;background:var(--blue)}

/* explore */
.grid{position:absolute;top:100px;left:28px;right:28px;display:grid;grid-template-columns:repeat(3,1fr);row-gap:30px}
.cat{display:flex;flex-direction:column;align-items:center;gap:8px;font-size:9px}
.cat i{width:34px;height:34px;border-radius:6px;background:var(--blue);box-shadow:0 6px 12px rgba(31,79,224,.3)}

/* messages */
.threads{position:absolute;top:78px;left:22px;right:22px}
.thread{height:42px;border-radius:6px;box-shadow:var(--card-shadow);margin-bottom:9px;display:flex;align-items:center;gap:8px;padding:0 10px;position:relative}
.thread b{display:block;font-size:9.5px}
.thread span{font-size:8px;color:var(--muted)}
.thread time{position:absolute;right:10px;top:9px;font-size:7px;color:var(--muted)}

/* profile */
.profile-head{position:absolute;top:68px;left:18px;right:18px;height:100px}
.profile-name{font-size:14px;font-weight:700}
.profile-count{font-size:9px;color:var(--blue);margin-top:3px}
.btn.small{width:34px;padding:3px 0;font-size:7.5px;border-radius:8px;margin-top:8px;box-shadow:none}
.profile-photo{position:absolute;right:0;top:0;width:80px;height:70px;border-radius:4px;background:linear-gradient(135deg,#c9ced8,#8e97a8)}
.settings-row{display:flex;justify-content:space-between;align-items:center;font-size:9px;margin-top:8px}
.toggle{width:24px;height:12px;border-radius:6px;background:var(--blue);position:relative}
.toggle::after{content:"";position:absolute;right:2px;top:2px;width:8px;height:8px;border-radius:50%;background:#fff}
</style>
</head>
<body>

<div class="page-title">Velmor Redesign Concept</div>

<!-- Walkthrough -->
<section class="screen walk col1 row1">
  <div class="brand"><span class="brand-dot"></span><div class="center-text">Welcome to<b>Velmor</b></div></div>
  <div class="band"></div>
  <div class="intro">
    <h3>Introduction</h3>
    <p>This is the intro of Velmor app. On this carousel we'll briefly tell the users that what's this app is all about.<br>To begin with, the app let's you share and collect coupons and rewards on 100+ products in 14 categories.</p>
  </div>
  <div class="cta"><span class="btn white">Get Started</span></div>
</section>
<div class="caption col1 cap1">Walkthrough</div>

<!-- Signup -->
<section class="screen col2 row1">
  <svg class="back" viewBox="0 0 14 14"><path d="M9 2 4 7l5 5" fill="none" stroke="#1b1d2a" stroke-width="1.4"/></svg>
  <div class="topbar">Create Account</div>
  <div class="brand form-brand"><span class="brand-dot"></span><div class="center-text" style="font-size:10px">Signup to<b style="font-size:12px">Velmor</b></div></div>
  <div class="form-accent" style="top:198px;height:40px"></div>
  <div class="form-card" style="top:160px">
    <div class="field">Username</div>
    <div class="field">Email</div>
    <div class="field">Password<svg width="12" height="10" viewBox="0 0 12 10"><ellipse cx="6" cy="5" rx="5.5" ry="3.5" fill="none" stroke="#1f4fe0"/><circle cx="6" cy="5" r="1.6" fill="#1f4fe0"/></svg></div>
  </div>
  <div class="form-cta" style="top:465px"><span class="btn">Signup</span></div>
  <div class="switch-link" style="top:508px">Have an account? <b>Login</b></div>
</section>
<div class="caption col2 cap1">Signup</div>

<!-- Login -->
<section class="screen col3 row1">
  <svg class="back" viewBox="0 0 14 14"><path d="M9 2 4 7l5 5" fill="none" stroke="#1b1d2a" stroke-width="1.4"/></svg>
  <div class="topbar">Login</div>
  <div class="brand form-brand"><span class="brand-dot"></span><div class="center-text" style="font-size:10px">Login to<b style="font-size:12px">Velmor</b></div></div>
  <div class="form-accent" style="top:160px;height:40px"></div>
  <div class="form-card" style="top:160px">
    <div class="field">Email/username</div>
    <div class="field">Password</div>
  </div>
  <div class="forgot" style="top:240px">Forgot Password?</div>
  <div class="form-cta" style="top:465px"><span class="btn">Login</span></div>
  <div class="switch-link" style="top:508px">New here? <b>Signup</b></div>
</section>
<div class="caption col3 cap1">Login</div>

<!-- Home -->
<section class="screen col1 row2">
  <div class="brand-sm"><span class="brand-dot"></span></div>
  <svg class="search" viewBox="0 0 16 16"><circle cx="7" cy="7" r="5" fill="none" stroke="#1f4fe0" stroke-width="1.6"/><path d="m11 11 4 4" stroke="#1f4fe0" stroke-width="1.6"/></svg>
  <div class="peek-l"></div><div class="peek-r"></div>
  <div class="banner">All New and<br>Improved App!<span class="stripe"></span></div>
  <div class="dots"><i></i><i class="on"></i><i></i></div>
  <div class="list" style="top:212px">
    <div class="section-head">Featured Listings<span>View All</span></div>
    <div class="item"><div class="item-name">Brewhaus<em>— $5 Off</em></div><div class="item-meta">☆ 3.2</div><div class="item-meta">Added by <span class="mini-avatar"></span></div><span class="badge round"></span></div>
    <div class="item"><div class="item-name">Lumen Editor<em>— 20% Off</em></div><div class="item-meta">☆ 5</div><div class="item-meta">Added by <span class="mini-avatar"></span></div><span class="badge square"></span></div>
    <div class="item"><div class="item-name">Goldarch<em>— $15 Off</em></div><div class="item-meta">☆ 1</div><div class="item-meta">Added by <span class="mini-avatar"></span></div><span class="badge gold"></span></div>
  </div>
  <nav class="nav">
    <div class="nav-item"><svg width="12" height="12" viewBox="0 0 12 12"><path d="M1 6 6 1l5 5v5H1z" fill="none" stroke="#1f4fe0" stroke-width="1.2"/></svg>HOME</div>
    <div class="nav-item"><svg width="12" height="12" viewBox="0 0 12 12"><g fill="none" stroke="#8a8fa3"><rect x="1" y="1" width="4" height="4"/><rect x="7" y="1" width="4" height="4"/><rect x="1" y="7" width="4" height="4"/><rect x="7" y="7" width="4" height="4"/></g></svg></div>
    <div class="nav-plus"><svg width="10" height="10" viewBox="0 0 10 10"><path d="M5 0v10M0 5h10" stroke="#fff" stroke-width="1.6"/></svg></div>
    <div class="nav-item"><svg width="12" height="12" viewBox="0 0 12 12"><path d="M1 2h10v6H5l-3 3V8H1z" fill="none" stroke="#8a8fa3"/></svg></div>
    <div class="nav-item"><svg width="12" height="12" viewBox="0 0 12 12"><g fill="none" stroke="#8a8fa3"><circle cx="6" cy="4" r="2.5"/><path d="M1 11c1-3 9-3 10 0"/></g></svg></div>
  </nav>
</section>
<div class="caption col1 cap2">Home Screen</div>

<!-- Details -->
<section class="screen col2 row2">
  <svg class="back" viewBox="0 0 14 14"><path d="M9 2 4 7l5 5" fill="none" stroke="#1b1d2a" stroke-width="1.4"/></svg>
  <div class="topbar">Details</div>
  <div class="detail-body">
    <div class="detail-title">Lumen Editor</div>
    <div class="detail-sub">20% Off on Single user license<br>☆ 5</div>
    <div class="detail-img" role="img" aria-label="Product image"></div>
    <div class="label">Added By</div>
    <div class="added"><span class="avatar" role="img" aria-label="User photo"></span>Owen Reyes<span class="ring"></span></div>
    <div class="label">Tags</div>
    <div class="tags"><span class="tag">Software</span><span class="tag">Tools</span><span class="tag">Code</span><span class="tag">Discount</span><span class="tag">License</span></div>
    <div class="label">Description</div>
    <p class="para">Get 20% Off on your single user license purchase using this link:</p>
    <span class="link">https://lumen.example/buy</span>
    <div class="label">Special Instructions</div>
    <p class="para">Use the following link to get 20% Off on Your single user license.</p>
  </div>
</section>
<div class="caption col2 cap2">Details Screen</div>

<!-- Add New -->
<section class="screen col3 row2">
  <svg class="back" viewBox="0 0 14 14"><path d="M9 2 4 7l5 5" fill="none" stroke="#1b1d2a" stroke-width="1.4"/></svg>
  <div class="topbar">Add New</div>
  <div class="form-accent" style="top:230px;height:100px"></div>
  <div class="add-card">
    <div class="field">Name</div>
    <div class="field img"><span class="img-icon"></span>Add Image(s)</div>
    <div class="field tall">Description</div>
    <div class="field">Promotion</div>
    <div class="field">Reward</div>
    <div class="field">Tags</div>
    <div class="field tall">Special Instructions</div>
  </div>
  <div class="form-cta" style="top:490px"><span class="btn">Add</span></div>
</section>
<div class="caption col3 cap2">Adding Now</div>

<!-- Explore -->
<section class="screen col1 row3">
  <div class="brand-sm"><span class="brand-dot"></span></div>
  <svg class="search" viewBox="0 0 16 16"><circle cx="7" cy="7" r="5" fill="none" stroke="#1f4fe0" stroke-width="1.6"/><path d="m11 11 4 4" stroke="#1f4fe0" stroke-width="1.6"/></svg>
  <div class="grid">
    <div class="cat"><i></i>Games</div><div class="cat"><i></i>Shopping</div><div class="cat"><i></i>Movies</div>
    <div class="cat"><i></i>Food</div><div class="cat"><i></i>Music</div><div class="cat"><i></i>Fashion</div>
    <div class="cat"><i></i>Business</div><div class="cat"><i></i>Traveling</div><div class="cat"><i></i>Festivals</div>
  </div>
  <nav class="nav">
    <div class="nav-item"><svg width="12" height="12" viewBox="0 0 12 12"><path d="M1 6 6 1l5 5v5H1z" fill="none" stroke="#8a8fa3" stroke-width="1.2"/></svg></div>
    <div class="nav-item"><svg width="12" height="12" viewBox="0 0 12 12"><g fill="none" stroke="#1f4fe0"><rect x="1" y="1" width="4" height="4"/><rect x="7" y="1" width="4" height="4"/><rect x="1" y="7" width="4" height="4"/><rect x="7" y="7" width="4" height="4"/></g></svg>EXPLORE</div>
    <div class="nav-plus"><svg width="10" height="10" viewBox="0 0 10 10"><path d="M5 0v10M0 5h10" stroke="#fff" stroke-width="1.6"/></svg></div>
    <div class="nav-item"><svg width="12" height="12" viewBox="0 0 12 12"><path d="M1 2h10v6H5l-3 3V8H1z" fill="none" stroke="#8a8fa3"/></svg></div>
    <div class="nav-item"><svg width="12" height="12" viewBox="0 0 12 12"><g fill="none" stroke="#8a8fa3"><circle cx="6" cy="4" r="2.5"/><path d="M1 11c1-3 9-3 10 0"/></g></svg></div>
  </nav>
</section>
<div class="caption col1 cap3">Explore</div>

<!-- Messages -->
<section class="screen col2 row3">
  <div class="brand-sm"><span class="brand-dot"></span></div>
  <svg class="search" viewBox="0 0 16 16"><circle cx="7" cy="7" r="5" fill="none" stroke="#1f4fe0" stroke-width="1.6"/><path d="m11 11 4 4" stroke="#1f4fe0" stroke-width="1.6"/></svg>
  <div class="threads">
    <div class="thread"><span class="avatar" role="img" aria-label="User photo"></span><div><b>Liam Ortega</b><span>Hi, How are you?</span></div><time>2 Days</time></div>
    <div class="thread"><span class="avatar" role="img" aria-label="User photo"></span><div><b>Ethan Brooks</b><span>Hey Okay</span></div><time>2 Days</time></div>
    <div class="thread"><span class="avatar" role="img" aria-label="User photo"></span><div><b>Marcus Vale</b><span>Have I the meeting</span></div><time>2 Days</time></div>
    <div class="thread"><span class="avatar" role="img" aria-label="User photo"></span><div><b>Jonah Price</b><span>Hi do you know sport</span></div><time>2 Days</time></div>
    <div class="thread"><span class="avatar" role="img" aria-label="User photo"></span><div><b>Caleb Moreno</b><span>Lets meet</span></div><time>2 Days</time></div>
  </div>
  <nav class="nav">
    <div class="nav-item"><svg width="12" height="12" viewBox="0 0 12 12"><path d="M1 6 6 1l5 5v5H1z" fill="none" stroke="#8a8fa3" stroke-width="1.2"/></svg></div>
    <div class="nav-item"><svg width="12" height="12" viewBox="0 0 12 12"><g fill="none" stroke="#8a8fa3"><rect x="1" y="1" width="4" height="4"/><rect x="7" y="1" width="4" height="4"/><rect x="1" y="7" width="4" height="4"/><rect x="7" y="7" width="4" height="4"/></g></svg></div>
    <div class="nav-plus"><svg width="10" height="10" viewBox="0 0 10 10"><path d="M5 0v10M0 5h10" stroke="#fff" stroke-width="1.6"/></svg></div>
    <div class="nav-item"><svg width="12" height="12" viewBox="0 0 12 12"><path d="M1 2h10v6H5l-3 3V8H1z" fill="none" stroke="#1f4fe0"/></svg>CHATS</div>
    <div class="nav-item"><svg width="12" height="12" viewBox="0 0 12 12"><g fill="none" stroke="#8a8fa3"><circle cx="6" cy="4" r="2.5"/><path d="M1 11c1-3 9-3 10 0"/></g></svg></div>
  </nav>
</section>
<div class="caption col2 cap3">Messages</div>

<!-- Profile -->
<section class="screen col3 row3">
  <div class="brand-sm"><span class="brand-dot"></span></div>
  <svg class="search" viewBox="0 0 16 16"><circle cx="7" cy="7" r="5" fill="none" stroke="#1f4fe0" stroke-width="1.6"/><path d="m11 11 4 4" stroke="#1f4fe0" stroke-width="1.6"/></svg>
  <div class="profile-head">
    <div class="profile-name">Noah Carter</div>
    <div class="profile-count">15 Products</div>
    <span class="btn small">Edit</span>
    <div class="profile-photo" role="img" aria-label="Profile photo of the user"></div>
  </div>
  <div class="list" style="top:170px">
    <div class="section-head">My Posts<span>View All</span></div>
    <div class="item"><div class="item-name">Brewhaus<em>— $5 Off</em></div><div class="item-meta">☆ 3.2</div><div class="item-meta">Added by You</div><span class="badge round"></span></div>
  </div>
  <div class="list" style="top:272px">
    <div class="section-head">My Favorites<span>View All</span></div>
    <div class="item"><div class="item-name">Goldarch<em>— $15 Off</em></div><div class="item-meta">☆ 1</div><div class="item-meta">Added by <span class="mini-avatar"></span></div><span class="badge gold"></span></div>
  </div>
  <div class="list" style="top:380px">
    <div class="section-head">Settings</div>
    <div class="settings-row">Notifications<span class="toggle"></span></div>
  </div>
  <nav class="nav">
    <div class="nav-item"><svg width="12" height="12" viewBox="0 0 12 12"><path d="M1 6 6 1l5 5v5H1z" fill="none" stroke="#8a8fa3" stroke-width="1.2"/></svg></div>
    <div class="nav-item"><svg width="12" height="12" viewBox="0 0 12 12"><g fill="none" stroke="#8a8fa3"><rect x="1" y="1" width="4" height="4"/><rect x="7" y="1" width="4" height="4"/><rect x="1" y="7" width="4" height="4"/><rect x="7" y="7" width="4" height="4"/></g></svg></div>
    <div class="nav-plus"><svg width="10" height="10" viewBox="0 0 10 10"><path d="M5 0v10M0 5h10" stroke="#fff" stroke-width="1.6"/></svg></div>
    <div class="nav-item"><svg width="12" height="12" viewBox="0 0 12 12"><path d="M1 2h10v6H5l-3 3V8H1z" fill="none" stroke="#8a8fa3"/></svg></div>
    <div class="nav-item"><svg width="12" height="12" viewBox="0 0 12 12"><g fill="none" stroke="#1f4fe0"><circle cx="6" cy="4" r="2.5"/><path d="M1 11c1-3 9-3 10 0"/></g></svg>PROFILE</div>
  </nav>
</section>
<div class="caption col3 cap3">Profile</div>

</body>
</html>
```